Automotive Business Card Design

I would just like a automotive themed card. nothing too extravagant, but catchy.

needs to say something about doing roadside assistance,mobile repairs, Diesel repairs, and Fleet maintenance

it can be single sided or double sided. no preference there.

Industry/Entity Type

Automotive

Contact Information for Business Card

Dean Marwick
phone 519 374 2083
Name: Brightway Automotive & Diesel Repair

```html
<!DOCTYPE html>
<html lang="en">
<head>
<meta charset="utf-8">
<title>Brightway Automotive &amp; Diesel Repair – Business Card</title>
<link rel="stylesheet" href="https://fonts.googleapis.com/css2?family=PT+Sans+Narrow:wght@400;700&display=swap">
<style>
  :root {
    --backdrop: #2b2b2b;
    --steel-light: #e4e4e4;
    --steel-mid: #c9c9c9;
    --steel-dark: #a9a9a9;
    --band-light: rgba(120,120,120,0.14);
    --band-dark: rgba(90,90,90,0.22);
    --ink: #3a3a3a;
    --ink-deep: #1f1f1f;
    --accent: #d9782a;
    --art-tone: #4a4a4a;
  }
  html, body {
    margin: 0;
    width: 1200px;
    height: 720px;
    overflow: hidden;
    background: var(--backdrop);
  }
  .business-card {
    position: absolute;
    left: 50px;
    top: 46px;
    width: 1100px;
    height: 628px;
    border-radius: 6px;
    overflow: hidden;
    font-family: "PT Sans Narrow", "Arial Narrow", sans-serif;
    font-weight: 700;
    color: var(--ink);
    background:
      repeating-linear-gradient(0deg, rgba(255,255,255,0.05) 0 1px, rgba(0,0,0,0.035) 1px 2px, transparent 2px 3px),
      linear-gradient(115deg, var(--steel-dark) 0%, var(--steel-light) 30%, var(--steel-mid) 55%, var(--steel-light) 75%, var(--steel-dark) 100%);
    box-shadow: 0 10px 30px rgba(0,0,0,0.5);
  }
  .art-truck-outline, .art-car-outline {
    position: absolute;
    border-radius: 8px;
    background: linear-gradient(180deg, rgba(70,70,70,0.25), rgba(70,70,70,0.1));
  }
  .art-truck-outline { left: 600px; top: 28px; width: 160px; height: 96px; }
  .art-car-outline { left: 110px; top: 120px; width: 250px; height: 56px; }
  .company-name {
    position: absolute;
    left: 86px;
    top: 178px;
    margin: 0;
    font-size: 50px;
    line-height: 1;
    color: var(--accent);
    letter-spacing: 0.5px;
  }
  .address {
    position: absolute;
    left: 350px;
    top: 254px;
    margin: 0;
    font-size: 26px;
    color: var(--ink);
  }
  .contact-band {
    position: absolute;
    left: 0; right: 0;
    top: 300px;
    height: 150px;
    background: var(--band-light);
  }
  .person-name {
    position: absolute;
    left: 80px;
    top: 330px;
    margin: 0;
    font-size: 40px;
    color: var(--ink);
  }
  .person-phone {
    position: absolute;
    left: 84px;
    top: 376px;
    margin: 0;
    font-size: 26px;
    color: var(--accent);
  }
  .service-list {
    position: absolute;
    left: 80px;
    right: 60px;
    top: 412px;
    margin: 0;
    padding: 0;
    list-style: none;
    display: flex;
    justify-content: space-between;
    font-size: 28px;
    color: var(--ink);
  }
  .service-list .sep { color: var(--accent); }
  .icon-band {
    position: absolute;
    left: 0; right: 0;
    top: 450px;
    bottom: 0;
    background: var(--band-dark);
  }
  .service-icons {
    position: absolute;
    left: 80px;
    right: 60px;
    top: 480px;
    display: flex;
    justify-content: space-between;
    align-items: center;
  }
  .service-icon {
    height: 90px;
    border-radius: 10px;
    background: linear-gradient(180deg, var(--art-tone), var(--ink-deep));
  }
  .icon-truck { width: 190px; }
  .icon-mobile { width: 140px; }
  .icon-roadside { width: 150px; }
  .icon-fleet { width: 170px; }
  .icon-diagnostics { width: 120px; }
</style>
</head>
<body>
  <main class="business-card">
    <div class="art-truck-outline" role="img" aria-label="Line drawing of a semi truck cab"></div>
    <div class="art-car-outline" role="img" aria-label="Line drawing of a speeding car with motion lines"></div>

    <h1 class="company-name">Brightway Automotive &amp; Diesel Repair</h1>
    <p class="address">2245 W Quarry Rd Millbrook, TX 76154</p>

    <div class="contact-band"></div>
    <p class="person-name">Dean Marwick</p>
    <p class="person-phone">519 374 2083</p>

    <ul class="service-list">
      <li>Diesel Repairs</li><li class="sep">-</li>
      <li>Mobile Repairs</li><li class="sep">-</li>
      <li>Roadside Assistance</li><li class="sep">-</li>
      <li>Fleet Maintenance</li>
    </ul>

    <div class="icon-band"></div>
    <div class="service-icons">
      <div class="service-icon icon-truck" role="img" aria-label="Semi truck silhouette for diesel repairs"></div>
      <div class="service-icon icon-mobile" role="img" aria-label="Car with crossed wrench and screwdriver for mobile repairs"></div>
      <div class="service-icon icon-roadside" role="img" aria-label="Car with a detached wheel for roadside assistance"></div>
      <div class="service-icon icon-fleet" role="img" aria-label="Group of cars for fleet maintenance"></div>
      <div class="service-icon icon-diagnostics" role="img" aria-label="Computer showing an engine warning for diagnostics"></div>
    </div>
  </main>
</body>
</html>
```